I would like to purchase a customized version of a design you have previously submitted - https://www.artquarry.net/design/5291847<br/><br/>I need a design for a swimming pool business card. The services we provide are Maintenance, Repairs and Installations so if you include that in the card. I would also like my email bluecrestpoolsservice@maildrift.net, my address 48317 Corvella Dr. Larkmoor NV, phone number 530-617-2384. Id like to have the two o's in Bluecrest Pools look like an actual pool.

```html
<!DOCTYPE html>
<html lang="en">
<head>
<meta charset="utf-8">
<title>Bluecrest Pools — Business Card</title>
<link rel="stylesheet" href="https://fonts.googleapis.com/css2?family=Questrial&display=swap">
<style>
  :root {
    --stage: #d4d4d4;
    --card: #26292c;
    --pool-blue: #17a6e3;
    --silver: #c9cbcd;
    --muted: #cfd2d4;
    --rule: #8e9296;
    --panel-dark: #222528;
    --panel-light: #ffffff;
    --ink-dark: #2a2f33;
  }
  * { box-sizing: border-box; margin: 0; padding: 0; }
  html, body { width: 1200px; height: 1042px; overflow: hidden; }
  body {
    font-family: "Questrial", Arial, sans-serif;
    background: var(--stage);
    position: relative;
  }
  .stage {
    position: absolute; left: 0; top: 0; width: 1200px; height: 876px;
    display: flex; align-items: center; justify-content: center; gap: 70px;
  }
  .card {
    width: 470px; height: 269px;
    background: var(--card);
    border-radius: 3px;
    box-shadow: 0 14px 28px rgba(0,0,0,.18);
    position: relative;
  }
  .card-back { display: flex; align-items: center; justify-content: center; }
  .brand-name {
    font-weight: 400;
    letter-spacing: -1px;
    line-height: 1;
    white-space: nowrap;
  }
  .card-back .brand-name { color: var(--silver); font-size: 44px; }
  .card-front { padding: 30px 34px 0 34px; }
  .card-front .brand-name { color: var(--pool-blue); font-size: 50px; text-align: right; }
  .tagline {
    margin-top: 8px; text-align: right;
    color: var(--muted); font-size: 13.5px;
    white-space: nowrap;
  }
  .tagline .dot, .panel .dot { color: var(--pool-blue); }
  .card-rule { height: 1px; background: var(--rule); margin: 14px 0 14px; }
  .contact { color: var(--muted); font-size: 13px; }
  .contact-row {
    display: flex; align-items: center; gap: 8px;
    margin-bottom: 9px; white-space: nowrap;
  }
  .contact-row svg { width: 14px; height: 14px; fill: var(--pool-blue); flex: none; }
  .panel {
    position: absolute; top: 876px; height: 166px;
    display: flex; flex-direction: column; align-items: center; justify-content: center;
  }
  .panel-dark { left: 0; width: 595px; background: var(--panel-dark); }
  .panel-light { left: 595px; width: 605px; background: var(--panel-light); }
  .panel .brand-name { font-size: 64px; color: var(--pool-blue); }
  .panel .tagline { text-align: center; font-size: 17px; margin-top: 10px; }
  .panel-dark .tagline { color: var(--muted); }
  .panel-light .tagline { color: var(--ink-dark); }
</style>
</head>
<body>
  <section class="stage">
    <article class="card card-back">
      <p class="brand-name">Bluecrest Pools</p>
    </article>

    <article class="card card-front">
      <p class="brand-name">Bluecrest Pools</p>
      <p class="tagline"><span class="dot">•</span> Maintenance, Repairs &amp; Installations <span class="dot">•</span></p>
      <div class="card-rule"></div>
      <div class="contact">
        <div class="contact-row">
          <svg viewBox="0 0 24 24" aria-hidden="true"><path d="M6.6 10.8a15.1 15.1 0 0 0 6.6 6.6l2.2-2.2a1 1 0 0 1 1-.25 11.4 11.4 0 0 0 3.6.57 1 1 0 0 1 1 1V20a1 1 0 0 1-1 1A17 17 0 0 1 3 4a1 1 0 0 1 1-1h3.5a1 1 0 0 1 1 1c0 1.25.2 2.45.57 3.57a1 1 0 0 1-.25 1z"/></svg>
          <span>530-617-2384</span>
        </div>
        <div class="contact-row">
          <svg viewBox="0 0 24 24" aria-hidden="true"><path d="M12 3 2 12h3v8h5v-5h4v5h5v-8h3z"/></svg>
          <span>48317 Corvella Dr. Larkmoor NV.</span>
        </div>
        <div class="contact-row">
          <svg viewBox="0 0 24 24" aria-hidden="true"><path d="M2 5h20v14H2zm2 2v.5l8 5 8-5V7zm0 2.8V17h16V9.8l-8 5z"/></svg>
          <span>bluecrestpoolsservice@maildrift.net</span>
        </div>
      </div>
    </article>
  </section>

  <section class="panel panel-dark">
    <p class="brand-name">Bluecrest Pools</p>
    <p class="tagline"><span class="dot">•</span> Maintenance, Repairs &amp; Installations <span class="dot">•</span></p>
  </section>
  <section class="panel panel-light">
    <p class="brand-name">Bluecrest Pools</p>
    <p class="tagline"><span class="dot">•</span> Maintenance, Repairs &amp; Installations <span class="dot">•</span></p>
  </section>
</body>
</html>
```